UK landscaping company needs website

We, Brackwell Landscapes need a website design for a company based in Surrey, UK. The design should be bold and playful. We have three main areas of work driveways, paving and fencing. It shouldn't be too heavy in text and concentrate on the pictures from previous jobs we've completed. You may use stock images for the design, these can be changed if you are successful. Please don’t just copy the flyer it is just there to provide content.
We have a logo design which we would also like editing slightly.
Here are some of my local competitors
https://www.fernivalelandscapes.co.uk/

https://www.twinbirchgardendesign.com/

https://mallowbecklandscapes.co.uk/

Industry/Entity Type

Landscaping

Coding

Coded - Design and coding required

Number of Pages Required

3 page

Font styles to use
Sans Serif

Requirements
Must have
• Pictures of my previous jobs.
Must be mobile friendly
Easy to navigate
Nice to have
• Try to use different colours. It would be good to have some designs that aren’t just black and green.
I’d like some curves in the design.
Should not have
• We install hard landscaping. Think more building/construction and less plants and cutting grass.

```html
<!DOCTYPE html>
<html lang="en">
<head>
<meta charset="utf-8">
<title>Brackwell Landscapes</title>
<link rel="stylesheet" href="https://fonts.googleapis.com/css2?family=Oswald:wght@400;500;600;700&family=Open+Sans:wght@400;600;700&display=swap">
<style>
:root{
  --green:#6cb33f;
  --green-dark:#4f8f2a;
  --ink:#222222;
  --text:#6b6b6b;
  --light:#f4f4f4;
  --line:#e3e3e3;
  --dark:#1d1d1d;
  --white:#ffffff;
}
*{box-sizing:border-box;margin:0;padding:0}
html,body{width:1200px;height:4756px;overflow:hidden}
body{font-family:"Open Sans",Arial,sans-serif;color:var(--text);font-size:13px;line-height:1.7;background:var(--white)}
h1,h2,h3,h4,.oswald{font-family:"Oswald",Arial,sans-serif;color:var(--ink);font-weight:500}
.wrap{width:1040px;margin:0 auto;position:relative}
.label{display:block;font-size:10px;letter-spacing:2px;text-transform:uppercase;color:var(--green);text-align:center}
.section-title{font-size:30px;text-align:center;margin-top:2px}
.section-title::after{content:"";display:block;width:40px;height:2px;background:var(--green);margin:10px auto 0}
.btn{display:inline-block;background:var(--green);color:var(--white);font-family:"Oswald",sans-serif;font-size:12px;letter-spacing:1px;text-transform:uppercase;padding:10px 22px}
.more{font-family:"Oswald",sans-serif;font-size:11px;color:var(--green);letter-spacing:1px;text-transform:uppercase}
.photo{display:block}

/* hero */
.hero{position:relative;height:780px;background:linear-gradient(120deg,#5b5548 0%,#8a7a64 40%,#a08c70 60%,#6a5e4c 100%)}
.hero::before{content:"";position:absolute;inset:0;background:linear-gradient(90deg,rgba(20,20,20,.65) 0%,rgba(20,20,20,.25) 70%,rgba(20,20,20,.15) 100%)}
.topbar{position:relative;height:32px;background:rgba(0,0,0,.55);color:#ddd;font-size:11px}
.topbar .wrap{display:flex;gap:26px;align-items:center;height:32px}
.topbar span{display:flex;gap:6px;align-items:center}
.header{position:relative;height:88px}
.header .wrap{display:flex;justify-content:space-between;align-items:center;height:88px}
.logo{display:flex;align-items:center;gap:10px;font-family:"Oswald",sans-serif;font-size:22px;font-weight:600;color:var(--white);letter-spacing:1px;text-transform:uppercase}
.logo i{width:14px;height:14px;background:var(--green);display:block}
.nav{display:flex;gap:30px;font-family:"Oswald",sans-serif;font-size:12px;color:var(--white);letter-spacing:1px}
.nav .active{border:1px solid var(--green);color:var(--green);padding:4px 10px;margin:-5px -4px}
.hero-body{position:relative;padding-top:160px}
.hero-body .kicker{font-size:11px;letter-spacing:2px;color:var(--white);text-transform:uppercase;font-weight:600}
.hero h1{font-size:50px;line-height:1.15;color:var(--white);font-weight:600;margin:12px 0 18px;text-transform:uppercase;width:640px}
.hero h1 em{font-style:normal;color:var(--green)}
.hero p{color:#eee;width:580px;font-size:13px;margin-bottom:28px}
.slider-ctrl{position:absolute;right:0;top:-10px;display:flex;flex-direction:column;align-items:center;gap:10px;color:var(--white);font-family:"Oswald",sans-serif}
.slider-ctrl b{font-size:22px;font-weight:500}
.slider-ctrl i{width:2px;height:28px;background:rgba(255,255,255,.6)}

/* about */
.about{height:680px;padding-top:80px}
.about-grid{display:flex;gap:60px;margin-top:44px}
.about-photos{width:470px;display:grid;grid-template-columns:1fr 1fr;gap:10px}
.about-photos .photo{height:190px}
.about-photos .wide{grid-column:1/3;height:200px;position:relative;display:flex;align-items:center;justify-content:center}
.play{display:flex;align-items:center;gap:12px;color:var(--white);font-family:"Oswald",sans-serif;font-size:14px}
.play i{width:44px;height:44px;border-radius:50%;background:var(--green);display:flex;align-items:center;justify-content:center}
.about-text{width:510px;padding-top:10px}
.about-text p{margin-bottom:18px}
.about-boxes{display:flex;gap:16px;margin:8px 0 26px}
.about-box{flex:1;display:flex;align-items:center;border:1px solid var(--line);height:48px}
.about-box b{width:48px;height:48px;background:var(--green);color:var(--white);font-family:"Oswald",sans-serif;font-size:18px;display:flex;align-items:center;justify-content:center}
.about-box span{font-family:"Oswald",sans-serif;color:var(--green);font-size:14px;padding-left:14px}

/* cta */
.cta{height:240px;background:var(--green);color:var(--white)}
.cta .wrap{display:flex;justify-content:space-between;align-items:center;height:240px}
.cta h2{color:var(--white);font-size:27px;font-weight:600;text-transform:uppercase}
.cta p{width:660px;margin-top:8px;font-size:12px;color:#eaf6e1}
.cta-side{text-align:center}
.cta-side small{display:block;font-size:10px;letter-spacing:2px;text-transform:uppercase;margin-bottom:10px}
.cta-side .btn{background:var(--white);color:var(--green);padding:12px 28px}

/* services */
.services{height:640px;padding-top:78px}
.service-row{display:flex;gap:40px;margin-top:40px}
.service{flex:1}
.service .img-box{position:relative;height:200px}
.service .img-box .photo{height:200px}
.service .icon{position:absolute;left:-10px;bottom:-12px;width:44px;height:44px;background:var(--green);display:flex;align-items:center;justify-content:center}
.service h3{font-size:16px;color:var(--green);margin:26px 0 8px}
.service p{font-size:12px;margin-bottom:14px}
.explore{text-align:center;margin-top:34px;font-size:12px;color:var(--ink);text-decoration:underline}

/* testimonial */
.testimonial{position:relative;height:240px;background:linear-gradient(90deg,#2f4a22 0%,#3f5a2e 50%,#7a6a4e 100%)}
.testimonial::before{content:"";position:absolute;inset:0;background:linear-gradient(90deg,rgba(47,80,30,.9) 0%,rgba(60,95,40,.7) 60%,rgba(60,95,40,.1) 100%)}
.testimonial .wrap{position:relative;padding-top:62px}
.quote{display:flex;gap:14px;width:760px}
.quote b{font-family:"Oswald",sans-serif;color:var(--green);font-size:44px;line-height:.8}
.quote p{color:var(--white);font-size:14px;font-weight:600}
.testimonial h4{color:var(--green);font-size:18px;margin:26px 0 0 38px}
.testimonial small{display:block;margin-left:38px;color:#cfd9c8;font-size:10px;letter-spacing:1px;text-transform:uppercase}
.arrows{position:absolute;right:0;top:70px;display:flex;flex-direction:column;gap:6px}
.arrows i{width:34px;height:34px;background:var(--green);display:flex;align-items:center;justify-content:center}
.arrows i+i{background:var(--white)}

/* work */
.work{height:840px;padding-top:72px}
.filters{display:flex;justify-content:center;gap:6px;margin:26px 0 22px}
.filters span{font-family:"Oswald",sans-serif;font-size:11px;letter-spacing:1px;padding:6px 20px;color:var(--text);background:var(--light)}
.filters .on{background:var(--green);color:var(--white)}
.work-grid{display:grid;grid-template-columns:1fr 1fr;gap:14px}
.work-item{position:relative;height:260px}
.work-item .photo{height:260px}
.work-cap{position:absolute;left:0;right:0;bottom:0;height:52px;background:rgba(108,179,63,.92);padding:8px 18px;color:var(--white)}
.work-cap h4{color:var(--white);font-size:15px;line-height:1.3}
.work-cap small{font-size:9px;letter-spacing:1px;text-transform:uppercase}
.work-cap i{position:absolute;right:16px;top:17px}

/* partners */
.partners{height:240px;background:var(--green)}
.partners .wrap{display:flex;justify-content:space-between;align-items:center;height:240px;padding:0 40px}
.badge{width:130px;height:56px;border:2px solid rgba(255,255,255,.85)}
.badge.round{width:64px;height:64px;border-radius:50%}

/* contact */
.contact{height:680px;padding-top:72px}
.contact .wrap{display:flex;justify-content:space-between}
.contact-left{width:440px;padding-top:130px}
.contact-left h2{font-size:30px;margin-bottom:22px}
.contact-left p{margin-bottom:16px}
.form-card{width:470px;border:1px solid var(--line);box-shadow:0 4px 18px rgba(0,0,0,.06);padding:28px 32px 34px}
.form-card .label{margin-bottom:4px}
.form-card h3{font-size:28px;text-align:center;margin-bottom:30px}
.fields{display:grid;grid-template-columns:1fr 1fr;gap:14px}
.field{height:40px;border:1px solid var(--line);font-size:11px;color:#999;padding:10px 12px}
.field.full{grid-column:1/3;height:120px}
.form-card .btn{display:block;text-align:center;margin-top:20px;padding:13px}

/* footer */
.footer{height:356px;background:var(--light);padding-top:70px}
.footer .wrap{display:flex;gap:44px}
.fcol{width:215px}
.fcol h4{font-size:16px;margin-bottom:6px}
.fcol h4::after{content:"";display:block;width:30px;height:2px;background:var(--green);margin-top:6px}
.fcol p,.fcol li{font-size:11.5px;list-style:none;line-height:2.1}
.fcol .row{display:flex;align-items:center;gap:8px;font-size:11.5px;margin-top:6px}
.newsletter-input{display:flex;margin:14px 0 18px;height:36px}
.newsletter-input span{flex:1;background:var(--white);border:1px solid var(--line);font-size:11px;color:#999;padding:8px 10px}
.newsletter-input b{width:36px;background:var(--green);display:flex;align-items:center;justify-content:center}
.follow{display:flex;align-items:center;gap:6px;font-size:11.5px}
.follow i{width:22px;height:22px;background:var(--green);display:block}
.follow i:first-of-type{background:#9a9a9a}
.copyright{height:56px;background:var(--green);color:var(--white);text-align:center;font-size:11px;line-height:56px}
.copyright b{font-weight:700}
</style>
</head>
<body>

<section class="hero" role="img" aria-label="Photo of a worker in gloves laying block paving on a driveway">
  <div class="topbar">
    <div class="wrap">
      <span><svg width="11" height="11" viewBox="0 0 24 24"><path fill="#6cb33f" d="M6.6 10.8a15 15 0 006.6 6.6l2.2-2.2c.3-.3.7-.4 1-.2 1.1.4 2.3.6 3.6.6.6 0 1 .4 1 1V20c0 .6-.4 1-1 1A17 17 0 013 4c0-.6.4-1 1-1h3.5c.6 0 1 .4 1 1 0 1.3.2 2.5.6 3.6.1.3 0 .7-.2 1z"/></svg>01483 204 771</span>
      <span><svg width="12" height="10" viewBox="0 0 24 18"><path fill="#6cb33f" d="M0 0h24v18H0z"/><path fill="none" stroke="#333" stroke-width="2" d="M1 1l11 9 11-9"/></svg>hello@brackwelllandscapes.co.uk</span>
    </div>
  </div>
  <div class="header">
    <div class="wrap">
      <div class="logo"><i></i>Brackwell</div>
      <nav class="nav"><span class="active">[ HOME ]</span><span>ABOUT</span><span>DRIVEWAYS</span><span>FENCING</span><span>PAVING</span><span>CONTACT</span></nav>
    </div>
  </div>
  <div class="hero-body">
    <div class="wrap">
      <span class="kicker">Welcome to Brackwell Landscapes</span>
      <h1>Your provider of <em>all</em> aspects of hard &amp; soft landscaping</h1>
      <p>Quality driveways, paving and fencing built to last across Surrey. From first sketch to final slab, our skilled team plans every detail and leaves your home looking its very best.</p>
      <span class="btn">Our Services</span>
      <div class="slider-ctrl"><i></i><b>02</b><i></i></div>
    </div>
  </div>
</section>

<section class="about">
  <div class="wrap">
    <span class="label">Introduction</span>
    <h2 class="section-title">About Us</h2>
    <div class="about-grid">
      <div class="about-photos">
        <div class="photo" role="img" aria-label="Photo of a grey block paved driveway" style="background:linear-gradient(135deg,#b9b9b5,#8e8d88)"></div>
        <div class="photo" role="img" aria-label="Photo of close-up paving setts" style="background:linear-gradient(135deg,#a59d92,#7d7468)"></div>
        <div class="photo wide" role="img" aria-label="Photo of a landscaped garden with shrubs and a path" style="background:linear-gradient(135deg,#6f8a4a,#3f5a2a)">
          <span class="play"><i><svg width="14" height="14" viewBox="0 0 24 24"><path fill="#fff" d="M6 3l15 9-15 9z"/></svg></i>Watch Our Work</span>
        </div>
      </div>
      <div class="about-text">
        <p>We at Brackwell Landscapes are a professional, experienced landscaping business that delivers premium garden construction at an affordable price. We provide all aspects of hard and soft landscaping throughout Surrey and surrounding areas, from driveways to patios, fences and more.</p>
        <div class="about-boxes">
          <div class="about-box"><b>01</b><span>Soft Landscaping</span></div>
          <div class="about-box"><b>02</b><span>Hard Landscaping</span></div>
        </div>
        <p>We pride ourselves on excellent workmanship and attention to detail. Using only top quality materials, we ensure an outstanding and long lasting finish, installed with care by our trained team. Every project is planned around your home, your budget and your timeline.</p>
        <span class="more">Learn More &rsaquo;</span>
      </div>
    </div>
  </div>
</section>

<section class="cta">
  <div class="wrap">
    <div>
      <h2>Please call us now for a free estimate!</h2>
      <p>Get in touch today for a friendly, no obligation quote on your driveway, paving or fencing project. Our team will visit your property, talk through the options and give you a clear price with no hidden extras.</p>
    </div>
    <div class="cta-side"><small>Speak with us</small><span class="btn">Contact Now</span></div>
  </div>
</section>

<section class="services">
  <div class="wrap">
    <span class="label">Latest on offer</span>
    <h2 class="section-title">Our Services</h2>
    <div class="service-row">
      <div class="service">
        <div class="img-box"><div class="photo" role="img" aria-label="Photo of a grey slab driveway" style="background:linear-gradient(135deg,#c8c8c4,#8f9290)"></div><span class="icon"><svg width="20" height="20" viewBox="0 0 24 24"><path fill="none" stroke="#fff" stroke-width="2" d="M3 20h18M5 20V10l7-5 7 5v10"/></svg></span></div>
        <h3>Driveways Services</h3>
        <p>Hard wearing block, slab and resin driveways laid on a solid base for a clean finish.</p>
        <span class="more">Learn More &rsaquo;</span>
      </div>
      <div class="service">
        <div class="img-box"><div class="photo" role="img" aria-label="Photo of a timber panel fence" style="background:linear-gradient(135deg,#b06a34,#7a4220)"></div><span class="icon"><svg width="20" height="20" viewBox="0 0 24 24"><path fill="none" stroke="#fff" stroke-width="2" d="M5 21V6l2-3 2 3v15M15 21V6l2-3 2 3v15M3 10h18M3 16h18"/></svg></span></div>
        <h3>Fencing Services</h3>
        <p>Sturdy panel, featheredge and slatted fencing that adds privacy and lasting style.</p>
        <span class="more">Learn More &rsaquo;</span>
      </div>
      <div class="service">
        <div class="img-box"><div class="photo" role="img" aria-label="Photo of block paving in a herringbone pattern" style="background:linear-gradient(135deg,#a8a6a2,#6f6c68)"></div><span class="icon"><svg width="20" height="20" viewBox="0 0 24 24"><path fill="none" stroke="#fff" stroke-width="2" d="M3 3h8v8H3zM13 3h8v8h-8zM3 13h8v8H3zM13 13h8v8h-8z"/></svg></span></div>
        <h3>Paving Services</h3>
        <p>Patios and pathways in natural stone or porcelain, cut and laid with real precision.</p>
        <span class="more">Learn More &rsaquo;</span>
      </div>
    </div>
    <p class="explore">Click here to explore all services</p>
  </div>
</section>

<section class="testimonial" role="img" aria-label="Photo of a worker laying paving, shaded green">
  <div class="wrap">
    <div class="quote"><b>&ldquo;</b><p>I was very impressed by the quality of the work from this company, so courteous and professional. Will absolutely hire them again and will recommend them to everyone asking. Thank you guys!</p></div>
    <h4>Martin Hale</h4>
    <small>Satisfied Client</small>
    <div class="arrows">
      <i><svg width="12" height="12" viewBox="0 0 24 24"><path fill="none" stroke="#fff" stroke-width="3" d="M15 4l-8 8 8 8"/></svg></i>
      <i><svg width="12" height="12" viewBox="0 0 24 24"><path fill="none" stroke="#6cb33f" stroke-width="3" d="M9 4l8 8-8 8"/></svg></i>
    </div>
  </div>
</section>

<section class="work">
  <div class="wrap">
    <span class="label">Recent projects</span>
    <h2 class="section-title">Our Work</h2>
    <div class="filters"><span class="on">ALL</span><span>DRIVEWAY</span><span>FENCING</span><span>PAVING</span></div>
    <div class="work-grid">
      <div class="work-item"><div class="photo" role="img" aria-label="Photo of a large slab driveway" style="background:linear-gradient(135deg,#b5b6b3,#7e807e)"></div><div class="work-cap"><h4>Driveway</h4><small>Surrey &middot; Home Garden</small><i><svg width="14" height="14" viewBox="0 0 24 24"><circle cx="10" cy="10" r="7" fill="none" stroke="#fff" stroke-width="2"/><path stroke="#fff" stroke-width="2" d="M15 15l6 6"/></svg></i></div></div>
      <div class="work-item"><div class="photo" role="img" aria-label="Photo of a patio enclosed by new fencing" style="background:linear-gradient(135deg,#9c8a72,#5f5444)"></div><div class="work-cap"><h4>Fencing</h4><small>Surrey &middot; Home Garden</small><i><svg width="14" height="14" viewBox="0 0 24 24"><circle cx="10" cy="10" r="7" fill="none" stroke="#fff" stroke-width="2"/><path stroke="#fff" stroke-width="2" d="M15 15l6 6"/></svg></i></div></div>
      <div class="work-item"><div class="photo" role="img" aria-label="Photo of a swimming pool with paved surround" style="background:linear-gradient(135deg,#5aa0c8,#6d8a50)"></div><div class="work-cap"><h4>Paving</h4><small>Surrey &middot; Home Garden</small><i><svg width="14" height="14" viewBox="0 0 24 24"><circle cx="10" cy="10" r="7" fill="none" stroke="#fff" stroke-width="2"/><path stroke="#fff" stroke-width="2" d="M15 15l6 6"/></svg></i></div></div>
      <div class="work-item"><div class="photo" role="img" aria-label="Photo of stone steps leading to a patio" style="background:linear-gradient(135deg,#c9c7c2,#8d8a84)"></div><div class="work-cap"><h4>Driveway</h4><small>Surrey &middot; Home Garden</small><i><svg width="14" height="14" viewBox="0 0 24 24"><circle cx="10" cy="10" r="7" fill="none" stroke="#fff" stroke-width="2"/><path stroke="#fff" stroke-width="2" d="M15 15l6 6"/></svg></i></div></div>
    </div>
  </div>
</section>

<section class="partners">
  <div class="wrap">
    <span class="badge" role="img" aria-label="Partner badge"></span>
    <span class="badge" role="img" aria-label="Partner badge"></span>
    <span class="badge" role="img" aria-label="Partner badge"></span>
    <span class="badge" role="img" aria-label="Partner badge"></span>
    <span class="badge round" role="img" aria-label="Partner badge"></span>
  </div>
</section>

<section class="contact">
  <div class="wrap">
    <div class="contact-left">
      <h2>Drop Us a Line Here!</h2>
      <p>Tell us a little about your project and we will come back to you within one working day with advice and a date to visit.</p>
      <p>Whether it is a new driveway, a paved patio or a run of fencing, we are happy to help with any size of job across Surrey.</p>
    </div>
    <div class="form-card">
      <span class="label">Get in touch with Brackwell</span>
      <h3>Request a Free Quote</h3>
      <div class="fields">
        <span class="field">First Name*</span>
        <span class="field">Email Address*</span>
        <span class="field">Phone Number*</span>
        <span class="field">Subject*</span>
        <span class="field full">Enter Your Message Here</span>
      </div>
      <span class="btn">Send Your Message</span>
    </div>
  </div>
</section>

<footer class="footer">
  <div class="wrap">
    <div class="fcol">
      <h4>About Company</h4>
      <p>Brackwell Landscapes builds driveways, paving and fencing for homes across Surrey, with care in every job.</p>
      <div class="row"><svg width="11" height="11" viewBox="0 0 24 24"><path fill="#6cb33f" d="M6.6 10.8a15 15 0 006.6 6.6l2.2-2.2c.3-.3.7-.4 1-.2 1.1.4 2.3.6 3.6.6.6 0 1 .4 1 1V20c0 .6-.4 1-1 1A17 17 0 013 4c0-.6.4-1 1-1h3.5c.6 0 1 .4 1 1 0 1.3.2 2.5.6 3.6.1.3 0 .7-.2 1z"/></svg>01483 204 771</div>
      <div class="row"><svg width="12" height="10" viewBox="0 0 24 18"><path fill="#6cb33f" d="M0 0h24v18H0z"/><path fill="none" stroke="#f4f4f4" stroke-width="2" d="M1 1l11 9 11-9"/></svg>hello@brackwelllandscapes.co.uk</div>
    </div>
    <div class="fcol">
      <h4>Quick Links</h4>
      <ul><li>Home</li><li>About</li><li>Driveways</li><li>Fencing</li><li>Paving</li><li>Contact</li></ul>
    </div>
    <div class="fcol">
      <h4>Information</h4>
      <ul><li>Privacy Policy</li><li>Terms Of Use</li><li>Sitemap</li><li>Test Plan</li><li>Another Test Plan</li><li>Some Other Test Plan</li></ul>
    </div>
    <div class="fcol">
      <h4>Newsletter</h4>
      <p>Subscribe to our newsletter to get our latest news and project updates.</p>
      <div class="newsletter-input"><span>Your email address</span><b><svg width="12" height="12" viewBox="0 0 24 24"><path fill="#fff" d="M2 12l20-9-6 19-4-8z"/></svg></b></div>
      <div class="follow">Find Us Here: <i></i><i></i><i></i></div>
    </div>
  </div>
</footer>
<div class="copyright">Copyright &copy; 2024 <b>Brackwell Landscapes</b> &middot; All Rights Reserved</div>

</body>
</html>
```